Pure Palm tree rhum label design

We need a label design for a palm tree rhum named 'Voile Doré'. We have an original design and we need an enhancement or a new design that reflects the product. It is a liquor. The label should be bilingual (French and English). We have original design that gives an idea and can be used as starting point. The text on the label for the existing design has to show up in the new design. The text is uploaded too as well as the existing design.
Update:
- The design must use Oil Palm Tree and not Palm Tree. Sample Images are attached.
- The neck of the bottle has to have the name of the product: Voile Doré.
- The word 'Liqueur' goes between the volume (1L) and the percentage of alcohol (43% Vol).
- Back side text is provided: see document
- The following description goes between the English and the french version (front and back):
The word: L'Original
The representation of a palm oil tree
The word: Original.
An image is uploaded for that.
No mandatory Fonts or Color or Bakground.

Font styles to use
Serif
Sans Serif
Script

```html
<!DOCTYPE html>
<html lang="fr">
<head>
<meta charset="utf-8">
<title>Kalé Marin – étiquette</title>
<link rel="stylesheet" href="https://fonts.googleapis.com/css2?family=Marcellus&display=swap">
<style>
  :root {
    --label-black: #000000;
    --page-white: #ffffff;
    --palm-grey: #4b4b4d;
    --gold-light: #f7d774;
    --gold-mid: #e0b23a;
    --gold-deep: #b8861b;
  }
  html, body {
    margin: 0;
    padding: 0;
    width: 1200px;
    height: 481px;
    overflow: hidden;
    background: var(--page-white);
  }
  .label {
    position: relative;
    width: 1200px;
    height: 481px;
  }
  .label-shape {
    position: absolute;
    inset: 0;
    display: block;
  }
  .palm-emblem {
    position: absolute;
    left: 490px;
    top: 40px;
    width: 220px;
    height: 234px;
    background: radial-gradient(ellipse at 50% 35%, #5a5a5c 0%, var(--palm-grey) 60%, rgba(75,75,77,0) 72%);
    border-radius: 50% 50% 40% 40%;
  }
  .product-name {
    position: absolute;
    left: 0;
    right: 0;
    top: 268px;
    margin: 0;
    text-align: center;
    font-family: "Marcellus", serif;
    font-weight: 400;
    font-size: 104px;
    line-height: 1;
    letter-spacing: 2px;
    white-space: nowrap;
    background: linear-gradient(90deg, var(--gold-deep) 0%, var(--gold-light) 35%, var(--gold-mid) 60%, var(--gold-light) 80%, var(--gold-deep) 100%);
    -webkit-background-clip: text;
    background-clip: text;
    color: transparent;
  }
  .gold-rule {
    position: absolute;
    left: 0;
    top: 408px;
    width: 1200px;
    height: 8px;
    background: linear-gradient(90deg, var(--gold-deep) 0%, var(--gold-mid) 20%, var(--gold-light) 50%, var(--gold-mid) 80%, var(--gold-deep) 100%);
  }
</style>
</head>
<body>
  <main class="label">
    <svg class="label-shape" width="1200" height="481" viewBox="0 0 1182 474" preserveAspectRatio="none" aria-hidden="true">
      <path fill="var(--label-black)"
            d="M0,145 H310 C370,145 385,110 410,80 C460,20 520,2 592,2 C664,2 724,20 774,80 C799,110 814,145 874,145 H1182 V474 H0 Z"/>
    </svg>
    <div class="palm-emblem" role="img" aria-label="Grey oil palm tree illustration with fronds and fruit cluster"></div>
    <h1 class="product-name">Kalé Marin</h1>
    <div class="gold-rule"></div>
  </main>
</body>
</html>
```